11 x 11 Flyer Design for Social Media - Reverse Mortgages

62 or older?

A Reverse Mortgage
could be
Your Road to Financial Freedom

* No Monthly Payments
* No Income Requirements
* No Credit Score Requirements
* No Loss of Ownership

Receive cash by lump sum, monthly installments or a line of credit!!

Call us today for a Free Consultation!!
(800) 471-2965

Bluegate Financial Services, Inc.
NMLS #318760
www.bluegatehome.com

```html
<!DOCTYPE html>
<html lang="en">
<head>
<meta charset="utf-8">
<title>Reverse Mortgage Flyer</title>
<link rel="stylesheet" href="https://fonts.googleapis.com/css2?family=Outfit:wght@400;500;600;700;800&display=swap">
<style>
:root{
  --cream:#f3ede3;
  --rust:#bd5e2e;
  --brown:#4f3f31;
  --white:#ffffff;
  --text-light:#f6f0e6;
}
html,body{margin:0;padding:0;overflow:hidden;background:var(--cream);}
.flyer{position:relative;width:1200px;height:1200px;overflow:hidden;background:var(--cream);font-family:'Outfit',sans-serif;}
.decor{position:absolute;inset:0;width:1200px;height:1200px;}
.headline{position:absolute;top:58px;left:0;width:1200px;text-align:center;margin:0;color:var(--rust);font-weight:700;font-size:94px;letter-spacing:1px;line-height:1;}
.subhead{position:absolute;top:178px;left:0;width:1200px;text-align:center;margin:0;color:var(--brown);font-weight:800;font-size:46px;line-height:58px;letter-spacing:0.5px;}
.photo{position:absolute;border:4px solid var(--white);box-shadow:0 4px 12px rgba(0,0,0,.2);}
.photo-beach{left:34px;top:330px;width:270px;height:280px;transform:rotate(-4deg);background:linear-gradient(160deg,#b9c6cf,#f2f0ec 55%,#cfc6b8);}
.photo-car{left:228px;top:532px;width:270px;height:280px;transform:rotate(-12deg);background:linear-gradient(170deg,#9fb27a,#8e7a66 45%,#2d3540);}
.photo-thinker{left:442px;top:350px;width:270px;height:280px;transform:rotate(-12deg);background:linear-gradient(150deg,#9fd3c4,#6d4a38 55%,#b9d4e4);}
.photo-phone{left:652px;top:530px;width:270px;height:280px;transform:rotate(-12deg);background:linear-gradient(170deg,#f1e6e4,#a8714e 50%,#6b4632);}
.photo-selfie{left:856px;top:350px;width:300px;height:280px;transform:rotate(-12deg);background:linear-gradient(150deg,#6e9dc0,#5d4034 50%,#1f2a44);}
.benefits{position:absolute;top:843px;margin:0;padding:0;list-style:none;color:var(--rust);font-size:26px;font-weight:400;line-height:35px;text-align:center;}
.benefits li::before{content:"\2022";margin-right:8px;font-size:20px;}
.benefits-left{left:100px;width:380px;}
.benefits-right{left:680px;width:430px;}
.payout-band{position:absolute;left:72px;top:955px;width:1056px;height:66px;background:var(--brown);color:var(--text-light);display:flex;align-items:center;justify-content:center;font-size:30px;font-weight:700;font-style:italic;letter-spacing:.2px;}
.contact{position:absolute;left:38px;top:1103px;color:var(--rust);font-weight:600;font-size:22px;line-height:33px;margin:0;}
.company{position:absolute;right:41px;top:1080px;color:var(--rust);font-weight:600;font-size:22px;line-height:33px;margin:0;text-align:right;}
</style>
</head>
<body>
<div class="flyer">
  <svg class="decor" viewBox="0 0 1200 1200" aria-hidden="true">
    <path d="M0 0 H130 C60 40 40 110 40 180 C40 230 20 255 0 265 Z" fill="#4f3f31"/>
    <path d="M1010 0 H1200 V112 C1130 95 1060 60 1010 0 Z" fill="#bd5e2e"/>
    <path d="M462 1200 C560 1130 760 1120 862 1200 Z" fill="#bd5e2e"/>
    <path d="M0 360 C300 300 700 420 1200 320" stroke="#ebe4d8" stroke-width="40" fill="none"/>
    <path d="M0 900 C400 860 800 980 1200 880" stroke="#ece5da" stroke-width="30" fill="none"/>
  </svg>

  <h1 class="headline">62 OR OLDER?</h1>
  <h2 class="subhead">A REVERSE MORTGAGE COULD BE<br>YOUR ROAD TO FINANCIAL FREEDOM</h2>

  <div class="photo photo-beach" role="img" aria-label="Smiling senior couple in white on a beach"></div>
  <div class="photo photo-thinker" role="img" aria-label="Thoughtful senior man with hand at his chin"></div>
  <div class="photo photo-selfie" role="img" aria-label="Laughing senior couple taking a selfie"></div>
  <div class="photo photo-car" role="img" aria-label="Happy senior couple in a convertible car"></div>
  <div class="photo photo-phone" role="img" aria-label="Senior woman looking at her phone at home"></div>

  <ul class="benefits benefits-left">
    <li>No Monthly Payments</li>
    <li>No Income Requirements</li>
  </ul>
  <ul class="benefits benefits-right">
    <li>No Loss of Ownership</li>
    <li>No Credit Score Requirements</li>
  </ul>

  <div class="payout-band">Receive cash by lump sum, monthly installments or a line of credit!!</div>

  <p class="contact">Call us today for a Free Consultation!!<br>(800) 471-2965</p>
  <p class="company">Bluegate Financial Services, Inc.<br>NMLS #318760<br>www.bluegatehome.com</p>
</div>
</body>
</html>
```